Label for LiPo Battery Product for RC Hobby Industry

We need your creativity for a new lithium battery label design. We aim to make our product visually appealing and distinct from competitors. Your design skills are crucial for this task, and we're excited to work with you.
Our main label feature is the colour tag profile, designed to easily identify battery category and power level with a 2-way colour band. Inspired by a tool company that uses a consistent colour profile to identify Phillips head sizing across their range.
The design should be modern, clear, convey speed and suitable for both professional and consumer markets.
Target Market(s)
RC, Drone, Camera community. 20-30 year old.
Industry/Entity Type
Battery, Drone Industry, RC Car
Requirements
Must have
- 2-Way colour tag identity profiling, clear text at 100% scale
Nice to have
- Text and graphic alignment. Comfortable padding and formatting. Colour tag profile, clear text."
Should not have
- Basic, stock looking image.

```html
<!DOCTYPE html>
<html lang="en">
<head>
<meta charset="utf-8">
<title>X4280 Battery Label</title>
<link rel="stylesheet" href="https://fonts.googleapis.com/css2?family=Exo+2:ital,wght@0,700;0,800;1,800;1,900&display=swap">
<style>
  :root {
    --page: #ffffff;
    --navy-top: #0c1a78;
    --navy-deep: #020720;
    --red-bright: #ff0a06;
    --red-deep: #6a0000;
    --cyan: #00b8ec;
    --white: #ffffff;
    --bar-dark: #1c1c1c;
    --bar-light: #8a8a8a;
  }
  * { margin: 0; padding: 0; box-sizing: border-box; }
  html, body { width: 1200px; height: 1062px; overflow: hidden; background: var(--page); }
  .canvas { position: relative; width: 1200px; height: 1062px; }
  .label {
    position: absolute; left: 346px; top: 394px;
    width: 504px; height: 272px; overflow: hidden;
    font-family: "Exo 2", sans-serif; color: var(--white);
  }
  .label-bg { position: absolute; inset: 0; }
  .brand {
    position: absolute; left: 37px; top: 122px;
    transform: translate(-50%, -50%) rotate(-90deg);
    font-weight: 800; font-size: 43px; letter-spacing: 1px;
    line-height: 1; white-space: nowrap; color: var(--white);
  }
  .model {
    position: absolute; left: 104px; top: 2px; width: 370px;
    text-align: center;
    font-weight: 800; font-style: normal; font-size: 120px;
    line-height: 1; letter-spacing: 0; white-space: nowrap;
    color: var(--white);
  }
  .capacity {
    position: absolute; left: 216px; top: 120px;
    font-weight: 900; font-style: italic; font-size: 56px;
    line-height: 1; letter-spacing: -2px;
  }
  .specs {
    position: absolute; left: 110px; top: 194px; width: 358px;
    display: flex; justify-content: space-between; align-items: center;
    font-weight: 800; font-size: 17px; line-height: 1;
  }
  .specs .divider { width: 1px; height: 20px; background: var(--white); }
  .tagline {
    position: absolute; left: 0; right: 0; top: 240px; height: 32px;
    display: flex; align-items: center; justify-content: center; padding-left: 6px;
    font-weight: 700; font-size: 15px; white-space: nowrap;
  }
</style>
</head>
<body>
<div class="canvas">
  <div class="label">
    <svg class="label-bg" width="504" height="272" viewBox="0 0 504 272" aria-hidden="true">
      <defs>
        <linearGradient id="redBand" x1="0" y1="0" x2="0" y2="1">
          <stop offset="0" stop-color="var(--red-bright)"/>
          <stop offset="1" stop-color="var(--red-deep)"/>
        </linearGradient>
        <radialGradient id="navyField" cx="0.35" cy="0.1" r="0.9">
          <stop offset="0" stop-color="var(--navy-top)"/>
          <stop offset="0.6" stop-color="#06104a"/>
          <stop offset="1" stop-color="var(--navy-deep)"/>
        </radialGradient>
        <linearGradient id="bottomBar" x1="0" y1="0" x2="1" y2="0">
          <stop offset="0" stop-color="var(--bar-dark)"/>
          <stop offset="0.5" stop-color="var(--bar-light)"/>
          <stop offset="1" stop-color="var(--bar-dark)"/>
        </linearGradient>
        <linearGradient id="glowLine" x1="0" y1="0" x2="1" y2="0">
          <stop offset="0" stop-color="var(--cyan)" stop-opacity="0"/>
          <stop offset="0.45" stop-color="var(--cyan)"/>
          <stop offset="1" stop-color="var(--cyan)" stop-opacity="0"/>
        </linearGradient>
      </defs>
      <rect width="504" height="240" fill="url(#redBand)"/>
      <path d="M129 0 H504 V240 H129 C95 215 68 175 68 124 C68 72 95 25 129 0 Z" fill="url(#navyField)"/>
      <rect x="152" y="222" width="321" height="4" rx="2" fill="url(#glowLine)"/>
      <rect y="240" width="504" height="32" fill="url(#bottomBar)"/>
    </svg>
    <div class="brand">KAVELTA</div>
    <div class="model">X4280</div>
    <div class="capacity">1.3Ah</div>
    <div class="specs">
      <span>120C</span><span class="divider"></span>
      <span>6 CELLS</span><span class="divider"></span>
      <span>22.2V</span><span class="divider"></span>
      <span>1300WH</span>
    </div>
    <div class="tagline">Performance • Armour Protection • Advanced Insulation</div>
  </div>
</div>
</body>
</html>
```